Buchcover-Design für Fantasy-Serie
Inspirierte und saubere Umsetzung, sowie kundenorientiert auch bei Sonderwünschen.
Zielgruppe
Buchverlag (Kleinstverlag). Wir verlegen Bücher aus den Genres Fantasy / SciFi / Thriller und Kriminalroman, sowie spezielle thematische Ausgaben. Kern unserer Tätigkeit ist die Wiederveröffentlichung der Nebelhorn-Chronik des deutschen Fantasy Autors Konrad Tilling sowie eine SciFi Serie des deutschen Autor Enno Braxmeyer. Wir suchen genretypische Cover mit Whow-Effekt.
Aufgabenstellung
Bei unserem ersten Auftrag handelt es sich um eine Fantasy Serie, bestehend aus 8 Bänden, welche vorwiegend als Kindle / eBook aber auch als Paperback veröffentlicht werden. Das Titelmotiv stammt jedes Mal von Laurent Dubelcq (lizensiert) und ändert sich bei jedem Buch. Der Titel muss daher von uns bearbeitbar sein.
das EBook hat die üblichen Maße: 1600x2560, 72 dpi
Print wird voraussichtl. 12x19, aber wir benötigen nur den Titel in 300 DPI (identisch mit Ebook lediglich höhere Auflösung).
Text:
(Autorenname): Konrad Tilling
(Buchtitel): Der Zirkel von Quasmar
(Titelzusatz): Erster Roman der Nebelhorn-Chronik
(Gattung): Roman
(Verlagslogo): Wahlweise kleines oder großes Logo, farblich angepasst
Hinweis: bei Auftrag wird das Titelbild in hoher Auflösung von uns geliefert.

```html
<!DOCTYPE html>
<html lang="de">
<head>
<meta charset="utf-8">
<title>Der Zirkel von Quasmar – Umschlag</title>
<link href="https://fonts.googleapis.com/css2?family=Zilla+Slab:wght@300;400;700&family=Oswald:wght@300;400&family=Arvo:wght@700&display=swap" rel="stylesheet">
<style>
  :root {
    --stage-top: #0d3147;
    --stage-bottom: #0a1a2c;
    --ink-white: #ffffff;
    --cyan: #21b8ec;
    --band-blue: #0a8fc8;
    --band-teal: #0f6f86;
    --spine-black: #030507;
    --cloud-violet: #6b6491;
    --ground-dark: #1a1d25;
    --text-body: #e6eef2;
  }
  * { margin: 0; padding: 0; box-sizing: border-box; }
  html, body { width: 1200px; height: 1200px; overflow: hidden; }
  body {
    background: radial-gradient(ellipse at 50% 45%, var(--stage-top) 0%, var(--stage-bottom) 80%);
    position: relative;
    font-family: "Zilla Slab", serif;
  }
  .cover {
    position: absolute; left: 117px; top: 240px; width: 966px; height: 718px;
    box-shadow: 0 10px 30px rgba(0,0,0,.45);
    overflow: hidden;
  }
  .logo {
    color: var(--ink-white); font-family: "Zilla Slab", serif; font-weight: 400;
    letter-spacing: .04em; text-transform: uppercase; white-space: nowrap;
  }

  /* Rückseite */
  .back { position: absolute; left: 0; top: 0; width: 453px; height: 718px; }
  .back-art {
    position: absolute; inset: 0;
    background:
      radial-gradient(ellipse 110px 260px at 90px 260px, rgba(170,110,80,.55), transparent 70%),
      linear-gradient(180deg, #3a3560 0%, #262243 40%, #0c0e14 80%, #050608 100%);
  }
  .back-band {
    position: absolute; left: 134px; top: 0; width: 170px; height: 718px;
    background: linear-gradient(180deg, rgba(20,120,140,.45) 0 260px, rgba(15,111,134,.8) 260px 100%);
  }
  .back .logo { position: absolute; left: 134px; width: 170px; top: 226px; text-align: center; font-size: 15px; }
  .blurb {
    position: absolute; left: 148px; top: 284px; width: 142px;
    color: var(--text-body); font-size: 9.4px; line-height: 13.6px; text-align: justify;
  }
  .blurb p + p { margin-top: 13px; }

  /* Buchrücken */
  .spine {
    position: absolute; left: 453px; top: 0; width: 52px; height: 718px;
    background: linear-gradient(180deg, var(--spine-black) 0 110px, var(--band-blue) 150px 560px, var(--spine-black) 600px 100%);
  }
  .spine-vertical { position: absolute; writing-mode: vertical-rl; left: 0; width: 52px; }
  .spine .logo { top: 30px; height: 118px; font-size: 14px; line-height: 52px; text-align: center; }
  .spine-title {
    top: 184px; font-size: 26px; line-height: 52px; color: var(--ink-white);
    font-family: "Arvo", serif; font-weight: 700; white-space: nowrap;
  }
  .spine-title .light { color: var(--cyan); font-family: "Zilla Slab", serif; font-weight: 300; }
  .spine-author {
    top: 600px; height: 96px; display: flex; flex-direction: column; justify-content: center; align-items: center;
    gap: 3px; padding: 0 8px;
  }
  .spine-author .label {
    display: flex; align-items: center; gap: 5px; height: 100%;
    font-family: "Oswald", sans-serif; color: var(--cyan); font-size: 10px; letter-spacing: .08em; line-height: 12px;
  }
  .spine-author .label::before, .spine-author .label::after { content: ""; flex: 1; width: 1px; background: var(--ink-white); opacity: .7; }
  .spine-author .name { font-size: 12px; line-height: 14px; color: var(--ink-white); font-weight: 700; white-space: nowrap; }

  /* Vorderseite */
  .front { position: absolute; left: 505px; top: 0; width: 461px; height: 718px; }
  .front-art {
    position: absolute; inset: 0;
    background:
      radial-gradient(ellipse 90px 70px at 320px 260px, rgba(220,160,170,.35), transparent 70%),
      radial-gradient(ellipse 150px 90px at 60px 220px, rgba(200,180,220,.35), transparent 70%),
      linear-gradient(180deg, #4b4878 0%, var(--cloud-violet) 35%, #4a4a68 58%, #2b2d38 75%, var(--ground-dark) 100%);
  }
  .front-band {
    position: absolute; left: 153px; top: 0; width: 170px; height: 469px;
    background: linear-gradient(180deg, rgba(40,100,170,.35) 0, rgba(10,143,200,.75) 90px, rgba(10,143,200,.85) 230px, rgba(30,110,170,.6) 318px);
  }
  .front-band .subtitle-box {
    position: absolute; left: 0; bottom: 0; width: 170px; height: 151px;
    background: rgba(15,111,134,.82);
    display: flex; align-items: center; justify-content: center;
    font-family: "Oswald", sans-serif; font-weight: 400; font-size: 22px; line-height: 27px;
    color: var(--ink-white); text-align: center;
  }
  .front .logo { position: absolute; left: 153px; width: 170px; top: 30px; text-align: center; font-size: 16px; }
  .title {
    position: absolute; left: 0; width: 461px; top: 84px; text-align: center;
    color: var(--ink-white); line-height: 44px;
  }
  .title .strong { font-family: "Arvo", serif; font-weight: 700; font-size: 44px; display: block; }
  .title .light { font-family: "Zilla Slab", serif; font-weight: 300; font-size: 50px; color: var(--cyan); display: block; }
  .byline { position: absolute; left: 125px; width: 226px; top: 636px; text-align: center; }
  .byline .label {
    display: flex; align-items: center; gap: 8px;
    font-family: "Oswald", sans-serif; font-size: 15px; letter-spacing: .1em; color: var(--cyan);
  }
  .byline .label::before, .byline .label::after { content: ""; flex: 1; height: 1px; background: var(--ink-white); opacity: .8; }
  .byline .name {
    font-family: "Arvo", serif; font-weight: 700; font-size: 22px; letter-spacing: .16em;
    color: var(--ink-white); margin-top: 2px; white-space: nowrap;
  }
  .foot-bar { position: absolute; left: 125px; width: 226px; top: 698px; height: 20px; background: var(--band-teal); }
</style>
</head>
<body>
  <div class="cover">
    <section class="back">
      <div class="back-art" role="img" aria-label="Fantasy-Illustration: schwebende Frauengestalt mit wehendem Gewand über nächtlicher Landschaft"></div>
      <div class="back-band"></div>
      <div class="logo">Veldmark</div>
      <div class="blurb">
        <p>Lorem ipsum dolor sit amet, consectetuer adipiscing elit, sed diam nonummy nibh euismod tincidunt ut laoreet dolore magna aliquam erat volutpat. Ut wisi enim ad minim veniam, quis nostrud exerci tation ullamcorper suscipit lobortis nisl ut aliquip ex ea commodo consequat.</p>
        <p>Lorem ipsum dolor sit amet, consectetuer adipiscing elit, sed diam nonummy nibh euismod tincidunt ut laoreet dolore magna aliquam erat volutpat.</p>
      </div>
    </section>

    <section class="spine">
      <div class="spine-vertical logo">Veldmark</div>
      <div class="spine-vertical spine-title">Der&nbsp;<span class="light">Zirkel</span>&nbsp;von Quasmar</div>
      <div class="spine-vertical spine-author">
        <span class="label">Author</span>
        <span class="name">Konrad Tilling</span>
      </div>
    </section>

    <section class="front">
      <div class="front-art" role="img" aria-label="Fantasy-Illustration: Frauengestalt im Wind über Wolken und Flusslandschaft, schwebender Felsbrocken"></div>
      <div class="front-band">
        <div class="subtitle-box">Erster<br>Roman der<br>Nebelhorn<br>-Chronik</div>
      </div>
      <div class="logo">Veldmark</div>
      <h1 class="title">
        <span class="strong">Der</span>
        <span class="light">Zirkel</span>
        <span class="strong">von Quasmar</span>
      </h1>
      <div class="byline">
        <div class="label">Author</div>
        <div class="name">Konrad Tilling</div>
      </div>
      <div class="foot-bar"></div>
    </section>
  </div>
</body>
</html>
```